Business card design can get creative with spot gloss, foil, metallic details, colored edge details, different shapes, imprint, etc. Open to creativity. Needs to look professional, elegant, sophisticated, and current.
Also, needs to be easy to read for a 40+ clientele. No strange or hard to read fonts.
If we get exceptional designs for the individual items we have asked for from different designers, we will choose more than one winner.
We realize now, it may not be possible to get all of the individual items we asked for from the same designer and that is ok.
Thanks everyone, we are overwhelmed by great designs.
What we like is a horizontal layout, not vertical, clean lines or minimal wave design. We like the web site address in white print on black, so it stands out and does not get lost with all the other information.
We also like a straight edge over a rounded corner. Can be glossy- if so- we may list services not next appointment on the back. It's too difficult & not practical for the appointment to be on glossy paper- hard to write on. We may opt to then have a separate appointment card- matte finish.
We are leaning towards only listing our local phone number the 555-019-2846, it's getting too cluttered with both local and toll free number.
Keep in mind the basic design of the card has to look good and balanced to print the card with and without the managers name. So that way we have the basic design for the boutique card and can change the employee information/name as appropriate.
The small addition of a touch of purple we like, as in #164.
We just need it to have a professional look not a casual feel to it.
I want to show that we are cutting edge, hip and up on the latest technology to stay connected to our clients and make it easy for them to reach us.

```html
<!DOCTYPE html>
<html lang="en">
<head>
<meta charset="utf-8">
<title>The Renewal Studio – Business Cards</title>
<link href="https://fonts.googleapis.com/css2?family=Questrial&display=swap" rel="stylesheet">
<style>
  :root {
    --backdrop: #2a2a2a;
    --card: #ffffff;
    --lime: #8dc63f;
    --lime-dark: #6ea52a;
    --ink: #3a3a3a;
    --ink-soft: #6b6b6b;
    --rule: #cfcfcf;
    --black: #1a1a1a;
  }
  html, body {
    margin: 0;
    width: 1200px;
    height: 852px;
    overflow: hidden;
    background: var(--backdrop);
    font-family: "Questrial", "Century Gothic", sans-serif;
    color: var(--ink);
  }
  .stage { position: relative; width: 1200px; height: 852px; }
  .card {
    position: absolute;
    width: 520px;
    height: 300px;
    background: var(--card);
    border-radius: 16px;
    overflow: hidden;
  }
  .card--horizontal { left: 70px; top: 110px; }
  .card--stacked { left: 610px; top: 440px; }
  .card__swoosh { position: absolute; inset: 0; width: 100%; height: 100%; }

  .brand { position: absolute; display: flex; align-items: center; gap: 14px; }
  .brand__dot { width: 46px; height: 46px; border-radius: 50%; background: var(--lime); flex: none; }
  .brand__name { font-size: 30px; line-height: 0.95; color: var(--ink); letter-spacing: -0.5px; }

  .card--horizontal .brand { left: 34px; top: 108px; }
  .divider { position: absolute; left: 246px; top: 52px; width: 1px; height: 196px; background: var(--rule); }

  .person__name { color: var(--lime-dark); font-size: 15px; font-weight: 700; margin: 0; }
  .person__role { font-size: 11px; color: var(--ink-soft); margin: 2px 0 0; }
  .address { font-size: 11px; line-height: 1.45; color: var(--ink); margin: 0; }

  .contacts { list-style: none; padding: 0; margin: 0; font-size: 11px; }
  .contacts li { display: flex; align-items: center; gap: 6px; height: 16px; }
  .contacts svg { width: 11px; height: 11px; flex: none; }

  .card--horizontal .details { position: absolute; left: 262px; top: 62px; }
  .card--horizontal .address { margin-top: 22px; }
  .card--horizontal .contacts { margin-top: 20px; }

  .card--stacked .brand { left: 196px; top: 40px; }
  .card--stacked .brand__name { font-size: 34px; }
  .card--stacked .person { position: absolute; left: 96px; top: 176px; text-align: left; }
  .card--stacked .address { margin-top: 10px; }
  .card--stacked .contacts { position: absolute; left: 268px; top: 178px; }
</style>
</head>
<body>
<div class="stage">

  <section class="card card--horizontal">
    <svg class="card__swoosh" viewBox="0 0 520 300" aria-hidden="true">
      <path d="M360 0 H520 V110 C500 50 440 12 360 0 Z" fill="var(--lime)"/>
      <path d="M350 0 C440 10 505 55 520 120" fill="none" stroke="var(--black)" stroke-width="3"/>
      <path d="M0 200 V300 H150 C80 290 22 255 0 200 Z" fill="var(--lime)"/>
      <path d="M0 190 C18 250 70 290 160 300" fill="none" stroke="var(--black)" stroke-width="3"/>
    </svg>
    <div class="brand">
      <span class="brand__dot"></span>
      <span class="brand__name">the<br>renewal<br>studio</span>
    </div>
    <div class="divider"></div>
    <div class="details">
      <p class="person__name">Clara Benton</p>
      <p class="person__role">Manager</p>
      <p class="address">418 Harbor Lane, Suite 12<br>Palm Cove, GA 30417</p>
      <ul class="contacts">
        <li><svg viewBox="0 0 12 12"><path d="M2 1h2.5l1 3-1.5 1a6 6 0 0 0 3 3l1-1.5 3 1V10a1 1 0 0 1-1 1A9 9 0 0 1 1 2a1 1 0 0 1 1-1z" fill="var(--lime)"/></svg>(T) 800-555-0147</li>
        <li><svg viewBox="0 0 12 12"><rect x="3" y="0.5" width="6" height="11" rx="1.2" fill="var(--lime)"/><rect x="4" y="2" width="4" height="6.5" fill="#fff"/></svg>555-019-2846</li>
        <li><svg viewBox="0 0 12 12"><rect x="0.5" y="2" width="11" height="8" rx="1" fill="var(--lime)"/><path d="M1 3l5 3.5L11 3" fill="none" stroke="#fff" stroke-width="1"/></svg>clara@therenewalstudio.com</li>
        <li><svg viewBox="0 0 12 12"><circle cx="6" cy="6" r="5.5" fill="var(--lime)"/><path d="M1 6h10M6 0.5c-3 3-3 8 0 11M6 0.5c3 3 3 8 0 11" fill="none" stroke="#fff" stroke-width="0.8"/></svg>www.therenewalstudio.com</li>
      </ul>
    </div>
  </section>

  <section class="card card--stacked">
    <svg class="card__swoosh" viewBox="0 0 520 300" aria-hidden="true">
      <path d="M400 0 H520 V90 C505 45 460 10 400 0 Z" fill="var(--lime)"/>
      <path d="M390 0 C460 10 508 45 520 100" fill="none" stroke="var(--black)" stroke-width="3"/>
      <path d="M0 215 V300 H120 C60 292 18 262 0 215 Z" fill="var(--lime)"/>
      <path d="M0 205 C15 258 55 292 130 300" fill="none" stroke="var(--black)" stroke-width="3"/>
    </svg>
    <div class="brand">
      <span class="brand__dot"></span>
      <span class="brand__name">the<br>renewal<br>studio</span>
    </div>
    <div class="person">
      <p class="person__name">Clara Benton</p>
      <p class="person__role">Manager</p>
      <p class="address">418 Harbor Lane, Suite 12<br>Palm Cove, GA 30417</p>
    </div>
    <ul class="contacts">
      <li><svg viewBox="0 0 12 12"><path d="M2 1h2.5l1 3-1.5 1a6 6 0 0 0 3 3l1-1.5 3 1V10a1 1 0 0 1-1 1A9 9 0 0 1 1 2a1 1 0 0 1 1-1z" fill="var(--lime)"/></svg>(T) 800-555-0147</li>
      <li><svg viewBox="0 0 12 12"><rect x="3" y="0.5" width="6" height="11" rx="1.2" fill="var(--lime)"/><rect x="4" y="2" width="4" height="6.5" fill="#fff"/></svg>555-019-2846</li>
      <li><svg viewBox="0 0 12 12"><rect x="0.5" y="2" width="11" height="8" rx="1" fill="var(--lime)"/><path d="M1 3l5 3.5L11 3" fill="none" stroke="#fff" stroke-width="1"/></svg>clara@therenewalstudio.com</li>
      <li><svg viewBox="0 0 12 12"><circle cx="6" cy="6" r="5.5" fill="var(--lime)"/><path d="M1 6h10M6 0.5c-3 3-3 8 0 11M6 0.5c3 3 3 8 0 11" fill="none" stroke="#fff" stroke-width="0.8"/></svg>www.therenewalstudio.com</li>
    </ul>
  </section>

</div>
</body>
</html>
```